Tarrow Creek plumbing plumbing company business card design

Something sinilar to business card i upload it is my old business card design
And have a good watermark with the logo or majority of the logot in rhe background as watermark

Plumbing business similar to uploaded design with a nice watermark of the logo

Font styles to use
Script

Colors

Designer to choose colors to be used in the design.

```html
<!DOCTYPE html>
<html lang="en">
<head>
<meta charset="utf-8">
<title>Tarrow Creek Plumbing – Business Card</title>
<link href="https://fonts.googleapis.com/css2?family=Montserrat:wght@400;500;600;800&family=Dancing+Script:wght@700&display=swap" rel="stylesheet">
<style>
  :root {
    --backdrop: #d9d9d7;
    --card-blue: #1a86d0;
    --card-blue-deep: #136fb4;
    --card-black: #151515;
    --ink-navy: #0c1a2b;
    --white: #ffffff;
    --accent-blue: #2a8fd8;
    --muted: #b9c0c7;
    --watermark-light: rgba(255,255,255,.09);
    --watermark-dark: rgba(42,143,216,.13);
  }
  * { box-sizing: border-box; margin: 0; padding: 0; }
  html, body { width: 1200px; height: 675px; overflow: hidden; }
  body {
    background: var(--backdrop);
    font-family: "Montserrat", sans-serif;
    position: relative;
  }
  .card {
    position: absolute;
    top: 195px;
    width: 500px;
    height: 286px;
    border-radius: 4px;
    overflow: hidden;
    box-shadow: 0 10px 24px rgba(0,0,0,.22);
  }
  .card--front {
    left: 70px;
    background: linear-gradient(135deg, var(--card-blue) 0%, var(--card-blue-deep) 100%);
    color: var(--white);
  }
  .card--back {
    left: 630px;
    background: var(--card-black);
    color: var(--white);
  }
  .watermark {
    position: absolute;
    font-family: "Montserrat", sans-serif;
    font-weight: 800;
    text-transform: uppercase;
    line-height: .9;
    white-space: nowrap;
    pointer-events: none;
  }
  .card--front .watermark {
    right: -30px;
    bottom: -22px;
    font-size: 120px;
    color: var(--watermark-light);
    text-align: right;
  }
  .card--back .watermark {
    left: -24px;
    top: -18px;
    font-size: 120px;
    color: var(--watermark-dark);
  }
  .brand-name {
    position: relative;
    font-weight: 800;
    text-transform: uppercase;
    letter-spacing: 1px;
    line-height: 1.05;
  }
  .card--front .brand-name {
    position: absolute;
    left: 34px;
    top: 30px;
    font-size: 26px;
    color: var(--ink-navy);
  }
  .back-content {
    position: absolute;
    inset: 0;
    display: flex;
    flex-direction: column;
    align-items: center;
    justify-content: center;
    gap: 16px;
  }
  .card--back .brand-name {
    font-size: 30px;
    text-align: center;
    color: var(--white);
  }
  .holder {
    position: absolute;
    left: 34px;
    top: 130px;
    width: 220px;
    color: var(--ink-navy);
    padding-bottom: 6px;
    border-bottom: 2px solid var(--white);
    display: flex;
    align-items: baseline;
  }
  .holder__name {
    font-family: "Dancing Script", cursive;
    font-weight: 700;
    font-size: 22px;
  }
  .holder__sep { font-weight: 600; font-size: 14px; margin: 0 6px; }
  .holder__role { font-weight: 500; font-size: 14px; }
  .contact-list {
    position: absolute;
    left: 34px;
    top: 182px;
    list-style: none;
    font-size: 13px;
    font-weight: 500;
    line-height: 20px;
  }
  .contact-list li { display: flex; align-items: center; gap: 8px; }
  .contact-list svg { width: 11px; height: 11px; fill: var(--white); flex: none; }
  .licence {
    position: absolute;
    right: 30px;
    bottom: 26px;
    font-size: 12px;
    font-weight: 500;
  }
  .web-address {
    position: relative;
    font-size: 15px;
    font-weight: 500;
    color: var(--muted);
  }
  .web-address__domain { color: var(--accent-blue); font-weight: 600; }
</style>
</head>
<body>

  <section class="card card--front" aria-label="Business card front">
    <div class="watermark" aria-hidden="true">Tarrow<br>Creek</div>

    <div class="brand-name">Tarrow Creek<br>Plumbing</div>

    <div class="holder">
      <span class="holder__name">Daniel Hartley</span><span class="holder__sep">|</span><span class="holder__role">Director</span>
    </div>

    <ul class="contact-list">
      <li>
        <svg viewBox="0 0 24 24" aria-hidden="true"><path d="M6.6 10.8a15.1 15.1 0 0 0 6.6 6.6l2.2-2.2a1 1 0 0 1 1-.25 11.4 11.4 0 0 0 3.6.57 1 1 0 0 1 1 1V20a1 1 0 0 1-1 1A17 17 0 0 1 3 4a1 1 0 0 1 1-1h3.5a1 1 0 0 1 1 1c0 1.25.2 2.45.57 3.57a1 1 0 0 1-.25 1z"/></svg>
        0400 512 736
      </li>
      <li>
        <svg viewBox="0 0 24 24" aria-hidden="true"><path d="M2 5h20v14H2zm2 2v.5l8 5 8-5V7zm0 2.9V17h16V9.9l-8 5z"/></svg>
        info@tarrowcreekplumbing.com
      </li>
      <li>
        <svg viewBox="0 0 24 24" aria-hidden="true"><path d="M12 2a10 10 0 1 0 0 20 10 10 0 0 0 0-20zm6.9 6h-3a15.6 15.6 0 0 0-1.4-3.6A8 8 0 0 1 18.9 8zM12 4c.8 1.2 1.5 2.5 1.9 4h-3.8c.4-1.5 1.1-2.8 1.9-4zM4.3 14a8 8 0 0 1 0-4h3.4a16 16 0 0 0 0 4zm.8 2h3a15.6 15.6 0 0 0 1.4 3.6A8 8 0 0 1 5.1 16zm3-8h-3a8 8 0 0 1 4.4-3.6A15.6 15.6 0 0 0 8.1 8zM12 20c-.8-1.2-1.5-2.5-1.9-4h3.8c-.4 1.5-1.1 2.8-1.9 4zm2.3-6H9.7a14.7 14.7 0 0 1 0-4h4.6a14.7 14.7 0 0 1 0 4zm.2 5.6a15.6 15.6 0 0 0 1.4-3.6h3a8 8 0 0 1-4.4 3.6zM16.3 14a16 16 0 0 0 0-4h3.4a8 8 0 0 1 0 4z"/></svg>
        tarrowcreekplumbing.com.au
      </li>
    </ul>

    <div class="licence">Lic No: 408271c</div>
  </section>

  <section class="card card--back" aria-label="Business card back">
    <div class="watermark" aria-hidden="true">Tarrow<br>Creek</div>
    <div class="back-content">
      <div class="brand-name">Tarrow Creek<br>Plumbing</div>
      <div class="web-address">www.<span class="web-address__domain">tarrowcreekplumbing</span>.com.au</div>
    </div>
  </section>

</body>
</html>
```